Media and Film Company Needs a New Website

We produce highly stylized commercials and film pieces for our clients. We also produce live events, both corporate and theatrical. Looking for a site that can show off our client videos - have a polished way to show off our team, and be able to create pages to highlight our clients and give a full overview of our project/process with them. We design simple website for some of our clients - so we are very wordpress familiar, and would like something that doesn't feel like a template.

Target Market(s)

content creators, creative directors, production teams, marketing agencies

Industry/Entity Type

Film Production

Number of Pages Required

4 page

Font styles to use
Sans Serif

Requirements
Must have
• slick looking video embed (from YT or Vimeo)
• project pages - client snapshot (what we did for them, how we did it)
• nice landing page, have our company video reel on the page
• testimonials
• contact page
• ability to have photos as a background if we want
Nice to have
• polished clean look - look to our logo colors and linear elements
• we produce very stylized videos for our clients and our website should reflect that
Should not have
• template look or feel to it- please bring your flare to the project!
• take a look at our current site - zantorvo.com we need a better way to highlight our work and our clients

```html
<!DOCTYPE html>
<html lang="en">
<head>
<meta charset="utf-8">
<title>Zantorvo Media &amp; Entertainment — Testimonials</title>
<link href="https://fonts.googleapis.com/css2?family=Montserrat:wght@300;400;500;600&display=swap" rel="stylesheet">
<style>
  :root {
    --ink: #222222;
    --page: #ffffff;
    --rule: #dddddd;
    --text: #333333;
    --muted: #777777;
    --accent: #f2b705;
    --magenta: #d3126f;
    --cyan: #00aeef;
    --card: #e9e9e9;
    --button: #d6d6d6;
    --button-text: #b5b5b5;
    --frame: #444444;
  }
  * { box-sizing: border-box; margin: 0; padding: 0; }
  html, body { width: 684px; height: 1200px; overflow: hidden; }
  body { position: relative; background: var(--ink); font-family: "Montserrat", sans-serif; color: var(--text); }

  .site-header { position: absolute; left: 0; top: 0; width: 684px; height: 36px; background: var(--ink); z-index: 2; box-shadow: 0 2px 4px rgba(0,0,0,.4); }
  .brand { position: absolute; left: 43px; top: 12px; color: #fff; font-size: 11px; font-weight: 600; letter-spacing: .5px; }
  .main-nav a { position: absolute; top: 15px; color: #fff; font-size: 7px; text-decoration: none; letter-spacing: .2px; }
  .main-nav a.is-active { color: var(--accent); }
  .main-nav a.is-active::after { content: ""; position: absolute; left: 0; right: 0; top: 14px; height: 3px; background: var(--accent); }

  .hero { position: absolute; left: 0; top: 36px; width: 684px; height: 349px; overflow: hidden; }
  .hero-photo { position: absolute; inset: 0; background: radial-gradient(ellipse at 50% 30%, #f3d9a8 0%, #d9a250 35%, #9a6a22 70%, #5c3a10 100%); }
  .quote { position: absolute; font-size: 6.6px; line-height: 8.3px; text-align: justify; padding: 16px 10px 0 10px; }
  .quote cite { display: block; font-style: normal; margin-top: 9px; font-size: 6.4px; text-align: left; }
  .quote--featured { left: 78px; top: 206px; width: 261px; height: 109px; background: var(--magenta); color: #fff; }
  .quote--plain { top: 210px; height: 100px; background: #fff; color: var(--muted); padding-top: 14px; }
  .quote--plain cite { color: var(--muted); }

  .content { position: absolute; left: 36px; top: 385px; width: 612px; height: 768px; background: var(--page); }
  .row-label { position: absolute; left: 52px; font-size: 6.6px; letter-spacing: .3px; color: var(--text); }
  .divider { position: absolute; left: 0; width: 612px; height: 1px; background: var(--rule); }
  .thumb { position: absolute; }
  .thumb--framed { border: 3px solid var(--frame); }
  .thumb-art { position: absolute; inset: 0; }
  .thumb-play { position: absolute; left: 50%; top: 50%; width: 32px; height: 32px; margin: -16px 0 0 -16px; }
  .art-moth { background: linear-gradient(120deg, #6d5a4a 0%, #9b8fc9 45%, #e58ad7 75%, #f7c6ef 100%); }
  .art-meadow { background: linear-gradient(180deg, #9fd0f0 0%, #cfe6f2 45%, #7db24e 75%, #4b7f2a 100%); }
  .art-rock { background: linear-gradient(160deg, #c0d48a 0%, #a88a66 45%, #6b5a45 75%, #7aa648 100%); }

  .video-card { position: absolute; left: 314px; top: 33px; width: 116px; height: 131px; background: #f4f4f4; border: 3px solid #c8c8c8; border-radius: 3px; }
  .video-card .thumb { left: 3px; top: 3px; width: 104px; height: 76px; }
  .video-card h3 { position: absolute; left: 5px; top: 84px; font-size: 6.6px; font-weight: 400; }
  .video-card p { position: absolute; left: 5px; top: 94px; width: 100px; font-size: 4.2px; line-height: 5px; color: var(--muted); }

  .section-title { position: absolute; left: 0; width: 612px; top: 500px; text-align: center; font-size: 10px; letter-spacing: .6px; font-weight: 400; }
  .service { position: absolute; top: 541px; width: 119px; height: 175px; background: var(--card); text-align: center; }
  .service--active { background: var(--cyan); }
  .service svg { position: absolute; left: 50%; top: 4px; transform: translateX(-50%); }
  .service h3 { position: absolute; left: 0; right: 0; top: 54px; font-size: 9.4px; font-weight: 400; line-height: 12px; letter-spacing: .3px; color: var(--text); }
  .service--active h3 { top: 66px; }
  .service ul { position: absolute; left: 8px; right: 8px; top: 84px; list-style: none; font-size: 5px; line-height: 6.5px; color: #555; text-transform: uppercase; }
  .service--active h3, .service--active ul { color: #fff; }
  .service .cta { position: absolute; left: 20px; top: 148px; width: 80px; height: 18px; background: var(--button); color: var(--button-text); font-size: 5.4px; line-height: 18px; letter-spacing: .3px; }
  .service--active .cta { background: var(--ink); color: #fff; }

  .site-footer { position: absolute; left: 0; top: 1160px; width: 684px; height: 28px; }
  .copyright { position: absolute; left: 35px; top: 10px; font-size: 6.8px; color: #fff; letter-spacing: .2px; }
  .social { position: absolute; top: 4px; width: 18px; height: 18px; border-radius: 50%; border: 1.5px solid #fff; background: #2a6db3; }
</style>
</head>
<body>
  <header class="site-header">
    <div class="brand">ZANTORVO</div>
    <nav class="main-nav">
      <a href="#" style="left:169px">HOME</a>
      <a href="#" style="left:222px">PORTFOLIO</a>
      <a href="#" style="left:288px">ABOUT US</a>
      <a href="#" class="is-active" style="left:343px">TESTIMONIALS</a>
      <a href="#" style="left:421px">PRESS</a>
      <a href="#" style="left:478px">CONTACT</a>
    </nav>
  </header>

  <section class="hero">
    <div class="hero-photo" role="img" aria-label="Smiling woman with long blond hair in a blue patterned shirt, outdoors in warm autumn sunlight"></div>
    <blockquote class="quote quote--featured">
      Thank you very much for all the hard work and creativity that you devoted to the LCP video, which was moving and uplifting and captured the essence of what we try to do so very well. It made a strong and very positive impact on the guests at the dinner, and elicited many very favorable comments. I am grateful to you for the very significant contribution that you made to the success of our 18th annual Marion Hale Benefit, and for all your help to LCP.
      <cite>Daniel Avery, Executive Director, Larkfield Community Partners</cite>
    </blockquote>
    <blockquote class="quote quote--plain" style="left:353px;width:260px">
      Lorem ipsum dolor sit amet, consectetur adipisicing elit, sed do eiusmod tempor incididunt ut labore et dolore magna aliqua. Ut enim ad minim veniam, quis nostrud exercitation ullamco laboris nisi ut aliquip ex ea commodo consequat. Duis aute irure dolor in reprehenderit in voluptate velit esse cillum dolore eu fugiat nulla pariatur. Excepteur sint occaecat cupidatat non proident, sunt in culpa qui officia deserunt mollit anim id est laborum.
      <cite>Daniel Avery, Executive Director, Larkfield Community Partners</cite>
    </blockquote>
    <blockquote class="quote quote--plain" style="left:620px;width:260px">
      Lorem ipsum dolor sit amet, consectetur adipisicing elit, sed do eiusmod tempor incididunt ut labore et dolore magna aliqua. Ut enim ad minim veniam, quis nostrud exercitation ullamco laboris nisi ut aliquip ex ea commodo consequat. Duis aute irure dolor in reprehenderit in voluptate velit esse cillum dolore eu fugiat nulla pariatur. Excepteur sint occaecat cupidatat non proident, sunt in culpa qui officia deserunt mollit anim id est laborum.
      <cite>Daniel Avery, Executive Director, Larkfield Community Partners</cite>
    </blockquote>
  </section>

  <main class="content">
    <h2 class="row-label" style="top:15px;font-weight:400">RECENTLY ADDED</h2>
    <div class="thumb thumb--framed" style="left:53px;top:36px;width:110px;height:82px"><div class="thumb-art art-moth" role="img" aria-label="Animated film still: creature with a pink flower"></div><svg class="thumb-play" viewBox="0 0 32 32"><circle cx="16" cy="16" r="16" fill="#222" opacity=".85"/><path d="M12 9 L23 16 L12 23 Z" fill="#fff"/></svg></div>
    <div class="thumb thumb--framed" style="left:185px;top:36px;width:110px;height:82px"><div class="thumb-art art-meadow" role="img" aria-label="Animated film still: meadow under blue sky"></div><svg class="thumb-play" viewBox="0 0 32 32"><circle cx="16" cy="16" r="16" fill="#222" opacity=".85"/><path d="M12 9 L23 16 L12 23 Z" fill="#fff"/></svg></div>
    <article class="video-card">
      <div class="thumb"><div class="thumb-art art-rock" role="img" aria-label="Animated film still: characters on a rocky hillside"></div><svg class="thumb-play" viewBox="0 0 32 32"><circle cx="16" cy="16" r="16" fill="#222" opacity=".85"/><path d="M12 9 L23 16 L12 23 Z" fill="#fff"/></svg></div>
      <h3>Video Title.</h3>
      <p>Lorem ipsum dolor sit amet, consectetur adipisicing elit, sed do eiusmod tempor incididunt ut labore et dolore magna aliqua. Ut enim ad minim veniam, quis</p>
    </article>
    <div class="thumb thumb--framed" style="left:449px;top:36px;width:110px;height:82px"><div class="thumb-art art-moth" role="img" aria-label="Animated film still: creature with a pink flower"></div><svg class="thumb-play" viewBox="0 0 32 32"><circle cx="16" cy="16" r="16" fill="#222" opacity=".85"/><path d="M12 9 L23 16 L12 23 Z" fill="#fff"/></svg></div>
    <div class="divider" style="top:173px"></div>

    <h2 class="row-label" style="top:192px;font-weight:400">UPCOMING RELEASES</h2>
    <div class="thumb" style="left:56px;top:217px;width:104px;height:75px"><div class="thumb-art art-moth" role="img" aria-label="Animated film still: creature with a pink flower"></div><svg class="thumb-play" viewBox="0 0 32 32"><circle cx="16" cy="16" r="16" fill="#222" opacity=".85"/><path d="M12 9 L23 16 L12 23 Z" fill="#fff"/></svg></div>
    <div class="thumb" style="left:188px;top:217px;width:104px;height:75px"><div class="thumb-art art-meadow" role="img" aria-label="Animated film still: meadow under blue sky"></div><svg class="thumb-play" viewBox="0 0 32 32"><circle cx="16" cy="16" r="16" fill="#222" opacity=".85"/><path d="M12 9 L23 16 L12 23 Z" fill="#fff"/></svg></div>
    <div class="thumb" style="left:321px;top:217px;width:104px;height:75px"><div class="thumb-art art-rock" role="img" aria-label="Animated film still: characters on a rocky hillside"></div><svg class="thumb-play" viewBox="0 0 32 32"><circle cx="16" cy="16" r="16" fill="#222" opacity=".85"/><path d="M12 9 L23 16 L12 23 Z" fill="#fff"/></svg></div>
    <div class="thumb" style="left:452px;top:217px;width:104px;height:75px"><div class="thumb-art art-moth" role="img" aria-label="Animated film still: creature with a pink flower"></div><svg class="thumb-play" viewBox="0 0 32 32"><circle cx="16" cy="16" r="16" fill="#222" opacity=".85"/><path d="M12 9 L23 16 L12 23 Z" fill="#fff"/></svg></div>
    <div class="divider" style="top:331px"></div>

    <h2 class="row-label" style="top:353px;font-weight:400">HALL OF FAME</h2>
    <div class="thumb" style="left:56px;top:376px;width:104px;height:75px"><div class="thumb-art art-moth" role="img" aria-label="Animated film still: creature with a pink flower"></div><svg class="thumb-play" viewBox="0 0 32 32"><circle cx="16" cy="16" r="16" fill="#222" opacity=".85"/><path d="M12 9 L23 16 L12 23 Z" fill="#fff"/></svg></div>
    <div class="thumb" style="left:188px;top:376px;width:104px;height:75px"><div class="thumb-art art-meadow" role="img" aria-label="Animated film still: meadow under blue sky"></div><svg class="thumb-play" viewBox="0 0 32 32"><circle cx="16" cy="16" r="16" fill="#222" opacity=".85"/><path d="M12 9 L23 16 L12 23 Z" fill="#fff"/></svg></div>
    <div class="thumb" style="left:321px;top:376px;width:104px;height:75px"><div class="thumb-art art-rock" role="img" aria-label="Animated film still: characters on a rocky hillside"></div><svg class="thumb-play" viewBox="0 0 32 32"><circle cx="16" cy="16" r="16" fill="#222" opacity=".85"/><path d="M12 9 L23 16 L12 23 Z" fill="#fff"/></svg></div>
    <div class="thumb" style="left:452px;top:376px;width:104px;height:75px"><div class="thumb-art art-moth" role="img" aria-label="Animated film still: creature with a pink flower"></div><svg class="thumb-play" viewBox="0 0 32 32"><circle cx="16" cy="16" r="16" fill="#222" opacity=".85"/><path d="M12 9 L23 16 L12 23 Z" fill="#fff"/></svg></div>
    <div class="divider" style="top:484px"></div>

    <h2 class="section-title">WHAT WE DO</h2>

    <article class="service" style="left:54px">
      <svg width="46" height="40" viewBox="0 0 46 40"><rect x="0" y="18" width="9" height="12" fill="#f5a000"/><circle cx="20" cy="10" r="6" fill="#333"/><circle cx="32" cy="10" r="6" fill="#333"/><rect x="10" y="17" width="30" height="19" rx="2" fill="#333"/><circle cx="25" cy="26" r="5" fill="#fff"/><path d="M23.5 23.5 L28 26 L23.5 28.5 Z" fill="#6cbb3c"/></svg>
      <h3>FILM AND MEDIA<br>PRODUCTION</h3>
      <ul><li>Kelvra Creative Suite</li><li>Motion Graphics</li><li>4K Workflow</li><li>Direct to</li><li>Web/Vidstream</li></ul>
      <div class="cta">GET STARTED</div>
    </article>

    <article class="service service--active" style="left:183px">
      <svg width="40" height="30" viewBox="0 0 40 30"><rect x="2" y="10" width="36" height="18" fill="#333"/><rect x="2" y="3" width="36" height="6" fill="#333"/><path d="M6 3 L10 9 M14 3 L18 9 M22 3 L26 9 M30 3 L34 9" stroke="#fff" stroke-width="2"/><rect x="6" y="14" width="28" height="2" fill="#fff"/><rect x="6" y="20" width="28" height="2" fill="#fff"/></svg>
      <h3>LIVE PRODUCTION</h3>
      <ul><li>Theatrical Producing</li><li>Production</li><li>Management</li><li>Lighting &amp; Video Design</li><li>Audio System Design</li></ul>
      <div class="cta">GET STARTED</div>
    </article>

    <article class="service" style="left:311px">
      <svg width="30" height="44" viewBox="0 0 30 44"><rect x="8" y="0" width="14" height="24" rx="7" fill="#333"/><rect x="8" y="12" width="14" height="2" fill="#f5a000"/><rect x="8" y="15" width="14" height="2" fill="#6cbb3c"/><path d="M4 18 Q4 30 15 30 Q26 30 26 18" fill="none" stroke="#333" stroke-width="2.5"/><rect x="13.5" y="30" width="3" height="9" fill="#333"/><rect x="7" y="39" width="16" height="3" fill="#333"/></svg>
      <h3>PR, MARKETING<br>&amp; ADVERTISING</h3>
      <ul><li>Branding</li><li>Social Media</li><li>Media Relations and</li><li>Outreach</li><li>Street Teams</li></ul>
      <div class="cta">GET STARTED</div>
    </article>

    <article class="service" style="left:440px">
      <svg width="46" height="44" viewBox="0 0 46 44"><path d="M23 1 L29 16 L45 16 L32 26 L37 42 L23 32 L9 42 L14 26 L1 16 L17 16 Z" fill="#f5a400"/></svg>
      <h3 style="top:66px">EVENTS</h3>
      <ul><li>Event Production</li><li>Staffing &amp; Hiring</li><li>Manage RFPs</li><li>Sponsor Relations</li></ul>
      <div class="cta">GET STARTED</div>
    </article>
  </main>

  <footer class="site-footer">
    <p class="copyright">©2016 ZANTORVO MEDIA &amp; ENTERTAINMENT</p>
    <span class="social" style="left:523px" aria-label="Social link"></span>
    <span class="social" style="left:550px" aria-label="Social link"></span>
    <span class="social" style="left:577px;background:#c4202a" aria-label="Social link"></span>
    <span class="social" style="left:604px;background:#1aaea0" aria-label="Social link"></span>
    <span class="social" style="left:630px;background:#1e88c8" aria-label="Social link"></span>
  </footer>
</body>
</html>
```